Web Design for Harbor Lane Guild

We need a web design for Harbor Lane Guild. You can see more details about the kind of business that it deals with in this link: http://harborlaneguild.example/. The concept of the site is similar to http://www.kelvora.example/ and we are looking for a homepage design also similar to it.
The top navigation should have:
1) directory
2) articles
3) deals
4) forums
5) log in/register page.
It should also have a video, a slider, map & text as well as a call to action to a "why register page".
As part of the footer it should include:
1) about HLG
2) contact HGL
3) terms & conditions
4) privacy
The color palette for the site will be the UAE flag colors which are red, green, white and black.
Updates
Project Deadline Extended
Reason: We need more designs and options.
Keep sending in more creative designs. thanks.
Industry/Entity Type
Business
Look and feel
Each slider illustrates characteristics of the customer's brand and the style your logo design should communicate.

```html
<!DOCTYPE html>
<html lang="en">
<head>
<meta charset="utf-8">
<title>Harbor Lane Guild</title>
<link rel="stylesheet" href="https://fonts.googleapis.com/css2?family=Gelasio:wght@400;500&family=Mulish:wght@400;600&display=swap">
<style>
:root{
  --red:#d83a2a;
  --red-dark:#b92b1d;
  --green:#1f9a3e;
  --green-dark:#137a2c;
  --ink:#2b2b2b;
  --text:#444;
  --muted:#666;
  --page:#f2f2f2;
  --white:#fff;
  --footer:#1e1e1e;
  --footer-bar:#141414;
  --footer-text:#bdbdbd;
}
*{margin:0;padding:0;box-sizing:border-box}
html,body{width:1200px;height:1097px;overflow:hidden}
body{position:relative;background:var(--white);font-family:"Mulish",sans-serif;color:var(--text)}
.backdrop{position:absolute;left:0;top:0}
.abs{position:absolute}

.brand{left:189px;top:36px;display:flex;align-items:center;gap:10px}
.brand-dot{width:34px;height:34px;border-radius:50%;background:var(--green)}
.brand-name{font-family:"Mulish",sans-serif;font-weight:600;font-size:17px;color:var(--green);letter-spacing:.3px}

.account{right:189px;top:15px;font-size:12.5px;display:flex;gap:10px}
.account a{color:var(--green);text-decoration:none}
.account a::before{content:"•";margin-right:5px}

.nav{left:645px;top:57px;display:flex;align-items:center}
.nav a{font-family:"Gelasio",serif;font-size:14px;color:var(--ink);text-decoration:none;letter-spacing:.4px;margin-right:22px}
.nav a.active{background:linear-gradient(#e24a38,var(--red-dark));color:var(--white);height:35px;width:116px;display:flex;align-items:center;justify-content:center;margin-right:14px;box-shadow:0 1px 2px rgba(0,0,0,.25)}

.hero-shadow{left:280px;top:488px;width:640px;height:40px;background:radial-gradient(ellipse at center top,rgba(0,0,0,.18),rgba(0,0,0,0) 70%)}
.hero{left:189px;top:111px;width:822px;height:387px;border:1px solid #d4d4d4;background:linear-gradient(100deg,#eceeee 0%,#dfe3e3 35%,#8c8a84 55%,#3a3836 75%,#2a2826 100%);box-shadow:0 1px 3px rgba(0,0,0,.15)}
.welcome{left:197px;top:207px;width:376px;height:220px;background:rgba(255,255,255,.96);box-shadow:0 2px 6px rgba(0,0,0,.18);padding:22px 26px}
.welcome-kicker{font-size:16px;color:#555;letter-spacing:.5px}
.welcome-title{font-family:"Gelasio",serif;font-size:30px;font-weight:400;line-height:1.15;margin-top:2px}
.welcome-title .g{color:var(--green)} .welcome-title .k{color:var(--ink)} .welcome-title .r{color:var(--red)}
.welcome p{font-size:11.4px;line-height:17px;color:var(--muted);margin-top:4px}
.btn{display:inline-flex;align-items:center;justify-content:center;margin-top:12px;width:122px;height:31px;background:linear-gradient(#2bb04a,var(--green-dark));color:var(--white);font-size:13px;text-decoration:none;border-radius:2px;box-shadow:0 1px 2px rgba(0,0,0,.3)}

.section-title{left:189px;top:536px;width:822px;display:flex;align-items:center;gap:20px}
.section-title .rule{flex:1;height:4px;background:repeating-linear-gradient(135deg,#444 0 1px,transparent 1px 3px)}
.section-title h2{font-family:"Gelasio",serif;font-weight:500;font-size:20px;color:var(--red)}

.reasons{left:189px;top:591px;width:500px;list-style:none}
.reasons li{position:relative;padding-left:25px;font-size:12.4px;line-height:15.5px;color:#333;margin-bottom:10px}
.reasons li svg{position:absolute;left:0;top:1px}

.video{left:701px;top:585px;width:310px;height:194px;background:#111;border:1px solid #ccc}
.video-frame{position:absolute;left:0;top:0;width:100%;height:175px;background:radial-gradient(ellipse at 60% 55%,#4b4d3f,#22231d 60%,#0d0d0b 100%)}
.video-play{position:absolute;left:126px;top:64px}
.video-bar{position:absolute;left:0;bottom:0;width:100%;height:18px;background:#1a1a1a;border-top:3px solid #333;display:flex;align-items:center;padding:0 8px;gap:8px;font-size:5px;color:#999}

.footer{left:0;top:823px;width:1200px;height:233px;background:var(--footer)}
.footer-bar{left:0;top:1056px;width:1200px;height:41px;background:var(--footer-bar);display:flex;align-items:center;justify-content:center;font-size:11px;color:#aaa}
.footer h3{font-family:"Gelasio",serif;font-weight:400;font-size:18px;color:var(--red);margin-bottom:15px}
.sitemap{left:189px;top:850px}
.sitemap ul{list-style:none}
.sitemap li{font-size:12px;line-height:18px;color:var(--footer-text)}
.sitemap li.current{color:var(--red)}
.about{left:411px;top:850px;width:265px}
.about p{font-size:11.6px;line-height:13.7px;color:var(--footer-text)}
.about a{display:block;margin-top:12px;font-size:13px;color:var(--green);text-decoration:none}
.contact{left:765px;top:853px;width:250px}
.contact .row{display:flex;gap:12px;font-size:12px;line-height:17px;color:var(--footer-text);margin-bottom:9px}
.contact .row svg{flex:none;margin-top:1px}
</style>
</head>
<body>

<svg class="backdrop" width="1200" height="520" viewBox="0 0 1200 520" aria-hidden="true">
  <path d="M0 0H1200V390Q600 520 0 390Z" fill="var(--page)"/>
  <path d="M0 390Q600 520 1200 390" fill="none" stroke="#d6d6d6"/>
</svg>

<header>
  <div class="abs brand"><span class="brand-dot"></span><span class="brand-name">HARBOR LANE GUILD</span></div>
  <div class="abs account"><a href="#">Login</a><a href="#">Register</a></div>
  <nav class="abs nav">
    <a class="active" href="#">DIRECTORY</a>
    <a href="#">ARTICLES</a>
    <a href="#">DEALS</a>
    <a href="#">FORUMS</a>
  </nav>
</header>

<div class="abs hero-shadow"></div>
<div class="abs hero" role="img" aria-label="Photo of two smiling business professionals in an office"></div>
<div class="abs welcome">
  <div class="welcome-kicker">Welcome to</div>
  <div class="welcome-title"><span class="g">HARBOR</span> <span class="k">LANE</span> <span class="r">GUILD</span></div>
  <p>Lorem Ipsum is simply dummy text of the printing and typesetting industry. Lorem Ipsum has been the industry's standard dummy text ever since the 1500s, when an unknown printer took a galley of type and scrambled it to.</p>
  <a class="btn" href="#">Learn More</a>
</div>

<div class="abs section-title"><span class="rule"></span><h2>Why register Harbor Lane Guild</h2><span class="rule"></span></div>

<ul class="abs reasons">
  <li><svg width="14" height="14" viewBox="0 0 14 14"><circle cx="7" cy="7" r="7" fill="var(--green)"/><path d="M5.5 4l3 3-3 3" stroke="#fff" stroke-width="1.8" fill="none"/></svg>Harbor Lane Guild will allow you to maximize the potential of your member business.</li>
  <li><svg width="14" height="14" viewBox="0 0 14 14"><circle cx="7" cy="7" r="7" fill="var(--green)"/><path d="M5.5 4l3 3-3 3" stroke="#fff" stroke-width="1.8" fill="none"/></svg>An online business network platform.</li>
  <li><svg width="14" height="14" viewBox="0 0 14 14"><circle cx="7" cy="7" r="7" fill="var(--green)"/><path d="M5.5 4l3 3-3 3" stroke="#fff" stroke-width="1.8" fill="none"/></svg>Provide a supportive infrastructure to enable companies to access and engage in unlimited networking opportunities.</li>
  <li><svg width="14" height="14" viewBox="0 0 14 14"><circle cx="7" cy="7" r="7" fill="var(--green)"/><path d="M5.5 4l3 3-3 3" stroke="#fff" stroke-width="1.8" fill="none"/></svg>Build mutual business relationships with fellow member companies.</li>
  <li><svg width="14" height="14" viewBox="0 0 14 14"><circle cx="7" cy="7" r="7" fill="var(--green)"/><path d="M5.5 4l3 3-3 3" stroke="#fff" stroke-width="1.8" fill="none"/></svg>As a Harbor Lane Guild member, you will have the opportunity to improve business techniques, whilst collaborating with industry peers and fellow professionals.</li>
  <li><svg width="14" height="14" viewBox="0 0 14 14"><circle cx="7" cy="7" r="7" fill="var(--green)"/><path d="M5.5 4l3 3-3 3" stroke="#fff" stroke-width="1.8" fill="none"/></svg>The Harbor Lane Guild keeps you up to date with what's happening and where.</li>
</ul>

<div class="abs video">
  <div class="video-frame" role="img" aria-label="Video still of a man seated at a desk with computer monitors"></div>
  <svg class="video-play" width="58" height="58" viewBox="0 0 58 58"><circle cx="29" cy="29" r="28" fill="#e8321f"/><path d="M22 16l20 13-20 13z" fill="#fff"/></svg>
  <div class="video-bar">
    <svg width="7" height="7" viewBox="0 0 7 7"><path d="M1 0l6 3.5L1 7z" fill="#999"/></svg>
    <span>0:00 / 6:39</span>
  </div>
</div>

<footer>
  <div class="abs footer"></div>
  <div class="abs sitemap">
    <h3>Site Map</h3>
    <ul>
      <li class="current">Home</li><li>About Us</li><li>Directory</li><li>Articles</li><li>Deals</li><li>Forums</li><li>Privacy</li><li>Terms &amp; Conditions</li>
    </ul>
  </div>
  <div class="abs about">
    <h3>About the Site</h3>
    <p>Lorem Ipsum is simply dummy text of the printing and typesetting industry. Lorem Ipsum has been the industry's standard dummy text ever since the 1500s, when an unknown printer took a galley of type and scrambled it to make a type specimen book. It has survived not only five centuries, but also the leap into electronic typesetting, remaining essentially unchanged.</p>
    <a href="#">Learn More....</a>
  </div>
  <div class="abs contact">
    <h3>Contact Us</h3>
    <div class="row"><svg width="16" height="17" viewBox="0 0 16 17"><path d="M8 1a5 5 0 0 0-5 5c0 4 5 10 5 10s5-6 5-10a5 5 0 0 0-5-5z" fill="var(--green)"/><circle cx="8" cy="6" r="2" fill="var(--footer)"/></svg><span>Level 12, Quayside Court, Tower 3,<br>Marrow Point Avenue,<br>Harbor District,</span></div>
    <div class="row"><svg width="16" height="16" viewBox="0 0 16 16"><path d="M3 1l3 3-1.5 2a9 9 0 0 0 5.5 5.5L12 10l3 3-2 2C7 15 1 9 1 3z" fill="var(--green)"/></svg><span>555 (0) 140 2281</span></div>
    <div class="row"><svg width="16" height="16" viewBox="0 0 16 16"><rect x="1" y="3" width="4" height="12" rx="1" fill="var(--green)"/><rect x="6" y="5" width="9" height="10" rx="1" fill="var(--green)"/><rect x="8" y="7" width="5" height="2" fill="var(--footer)"/></svg><span>+555 (0) 140 2290</span></div>
    <div class="row"><svg width="16" height="16" viewBox="0 0 16 16"><rect x="1" y="3" width="14" height="10" fill="var(--green)"/><path d="M1 3l7 6 7-6" stroke="var(--footer)" stroke-width="1.3" fill="none"/></svg><span>mira@harborlaneguild.example</span></div>
  </div>
  <div class="abs footer-bar">Copyright HARBOR LANE GUILD INC® 2003-13. All rights reserved</div>
</footer>

</body>
</html>
```